Business Card with many future opportunities awaiting

I work with many companies that have I need designers to develop quick projects for logo's business cards, banners etc. I would like to try Sketch hive for this simple project in hopes to come back and use the same designer for future projects.

This is a financial company that has many projects with lending services.

I need a business card made to be sleek somewhat modern, we will also need a simple logo made using The initials of the company KLT and maybe have an arrow going through the initials pointing up.

We like the colors purple, blue green or any rich colors ..but do not want the card to be to flashy. This is a conservative business..other colors or ideas can be used. They also want the card vertical or we can try horizontal front with logo and a vertical back with information.
Updates

These designs are much to modern for this company. Please be more conservative. Thank you so much!

Can you guys show some vertical designs rounded corners and light background darker colors. Not so bright

Target Market(s)

Very Wealthy Clients this card is for the Loan and Merchant Services

Industry/Entity Type

Conservative

Logo Text

KLT Velwick lending Allies (maybe with an arrow going up)

Font styles to use
Serif
Script

Requirements
Must have
• KLT
Velwick Lending Allies

Gerald Thornby
C.O.O.

7 Larkmoor Ave Suite4
Ashford Glen, NV 4417

555-204-6637 main
555-731-9082 cell
555-204-6638 fax

Ger@KLT.example
www.KLT.example

The final finals I will need to be able to make changes of names and numbers etc.
Nice to have
• I would like to have a spot for Notes on card if possible
Rounded corner edges

Client likes the royalty looking logo I have included maybe try and incorporate and change it up a bit. This logo was copied from somewhere else.

```html
<!DOCTYPE html>
<html lang="en">
<head>
<meta charset="utf-8">
<title>Velwick Lending Allies – Business Card</title>
<link rel="stylesheet" href="https://fonts.googleapis.com/css2?family=Oswald:wght@300;400;600&family=Questrial&display=swap">
<style>
  :root {
    --canvas: #ffffff;
    --navy-deep: #0f1229;
    --slate-blue: #3e4a6c;
    --glow: #8ec7d2;
    --mark-stone: #ddd8d0;
    --text-light: #e9eef0;
    --text-mist: #d3e4ea;
    --band-grey: #e3e8e9;
    --rule: #c3d3da;
  }
  * { margin: 0; padding: 0; box-sizing: border-box; }
  html, body { width: 1200px; height: 1000px; overflow: hidden; background: var(--canvas); }
  .canvas { position: relative; width: 1200px; height: 1000px; background: var(--canvas); }

  .card { position: absolute; top: 131px; width: 444px; height: 749px; overflow: hidden; }

  /* Front */
  .card-front {
    left: 88px;
    border-radius: 52px 0 52px 0;
    background: radial-gradient(ellipse 260px 330px at 52% 52%, var(--glow) 0%, #4d6a80 40%, #1e2540 75%, var(--navy-deep) 100%);
  }
  .front-mark {
    position: absolute; top: 232px; left: 0; width: 100%;
    text-align: center;
    font-family: "Oswald", sans-serif; font-weight: 400;
    font-size: 68px; letter-spacing: 6px; color: var(--mark-stone);
  }
  .front-company {
    position: absolute; top: 352px; left: 0; width: 100%;
    text-align: center;
    font-family: "Oswald", sans-serif; font-weight: 300;
    font-size: 24px; letter-spacing: 1.5px; color: var(--mark-stone);
    text-transform: uppercase;
  }
  .front-web {
    position: absolute; top: 690px; left: 0; width: 92%;
    text-align: center;
    font-family: "Questrial", sans-serif; font-size: 20px; color: var(--text-light);
  }

  /* Back */
  .card-back {
    left: 668px;
    border-radius: 0 50px 0 46px;
    background: radial-gradient(ellipse 250px 320px at 50% 51%, var(--glow) 0%, #5f8299 40%, #45557a 75%, var(--slate-blue) 100%);
  }
  .back-mark {
    position: absolute; top: 48px; right: 38px;
    font-family: "Oswald", sans-serif; font-weight: 400;
    font-size: 56px; letter-spacing: 5px; color: var(--mark-stone);
  }
  .back-company {
    position: absolute; top: 142px; right: 29px;
    font-family: "Oswald", sans-serif; font-weight: 300;
    font-size: 15px; letter-spacing: 0.8px; color: var(--text-light);
    text-transform: uppercase;
  }
  .holder { position: absolute; top: 240px; left: 100px; }
  .holder-name {
    font-family: "Oswald", sans-serif; font-weight: 600;
    font-size: 31px; line-height: 1.1; letter-spacing: 0.8px;
    color: var(--text-light); text-transform: uppercase;
  }
  .holder-title {
    font-family: "Questrial", sans-serif; font-size: 36px; line-height: 1.05;
    color: var(--navy-deep);
  }
  .holder-email {
    font-family: "Questrial", sans-serif; font-size: 20px; line-height: 1.3;
    color: var(--text-mist);
  }
  .notes { position: absolute; top: 372px; left: 65px; width: 340px; }
  .notes-line { height: 37px; border-bottom: 2px dotted var(--rule); }
  .contact {
    position: absolute; top: 517px; left: 65px;
    font-family: "Questrial", sans-serif; font-size: 23px; line-height: 31px;
    color: var(--text-light); list-style: none;
  }
  .back-foot-band {
    position: absolute; left: 0; bottom: 0; width: 100%; height: 48px;
    background: var(--band-grey);
  }
  .back-foot-tab {
    position: absolute; right: 0; bottom: 0; width: 280px; height: 57px;
    background: var(--navy-deep); border-radius: 40px 0 0 0;
    font-family: "Questrial", sans-serif; font-size: 24px;
    color: var(--text-light); line-height: 57px; padding-left: 42px;
    white-space: nowrap;
  }
</style>
</head>
<body>
<main class="canvas">
  <section class="card card-front" aria-label="Card front">
    <div class="front-mark">KLT</div>
    <div class="front-company">Velwick Lending Allies</div>
    <div class="front-web">www.KLT.example</div>
  </section>

  <section class="card card-back" aria-label="Card back">
    <div class="back-mark">KLT</div>
    <div class="back-company">Velwick Lending Allies</div>

    <div class="holder">
      <div class="holder-name">Gerald Thornby</div>
      <div class="holder-title">C.O.O.</div>
      <div class="holder-email">Ger@KLT.example</div>
    </div>

    <div class="notes" aria-label="Notes">
      <div class="notes-line"></div>
      <div class="notes-line"></div>
      <div class="notes-line"></div>
    </div>

    <ul class="contact">
      <li>7 Larkmoor Ave Suite4</li>
      <li>Ashford Glen, NV 4417</li>
      <li>Ph. 555-204-6637</li>
      <li>Cell. 555-731-9082</li>
      <li>Fax.555-204-6638</li>
    </ul>

    <div class="back-foot-band"></div>
    <div class="back-foot-tab">www.KLT.example</div>
  </section>
</main>
</body>
</html>
```